Website Design For Ecommerce Brand That Sells Personalized Wall Decor

We need a new website for our company Copper Lantern. Our current site is functioning through wordpress/woocomerce but we are not happy with the appearance. Our products really wow people when they receive them and we need your help making our website do the same!

Number of Pages Required

4 page

```html
<!DOCTYPE html>
<html lang="en">
<head>
<meta charset="utf-8">
<title>Copper Lantern — Personalized Wall Decor</title>
<link href="https://fonts.googleapis.com/css2?family=Jost:ital,wght@0,400;0,500;0,600;0,700;1,400&family=Great+Vibes&display=swap" rel="stylesheet">
<style>
:root{
  --teal:#4f9c86;
  --teal-dark:#3f8572;
  --orange:#e8823a;
  --brown:#8a4a1d;
  --brown-dark:#5a3418;
  --wood-light:#c9a27a;
  --wood-dark:#6e4528;
  --cream:#f7efdf;
  --cream-2:#fbf6ec;
  --ink:#2a2420;
  --muted:#6d655e;
  --line:#e6ded2;
  --white:#fff;
  --sale:#c8372d;
}
*{box-sizing:border-box;margin:0;padding:0}
html,body{width:1200px;height:4926px;overflow:hidden}
body{font-family:'Jost',sans-serif;color:var(--ink);background:var(--white);font-size:14px}
.container{width:885px;margin-left:158px;position:relative}
.script{font-family:'Great Vibes',cursive;font-weight:400}
.btn{display:inline-block;border-radius:6px;color:#fff;font-weight:600;font-size:13px;letter-spacing:.5px;text-transform:uppercase;text-align:center}
.btn--teal{background:var(--teal)}
.btn--orange{background:var(--orange)}
.ph{position:absolute}

/* top bar */
.topbar{height:34px;background:var(--teal);color:#fff;font-size:12px;display:flex;align-items:center;justify-content:center;gap:6px}
/* header */
.header{height:149px;position:relative;border-bottom:1px solid var(--line)}
.nav{position:absolute;left:158px;top:52px;width:306px;height:42px;border-top:1px solid var(--line);border-bottom:1px solid var(--line);display:flex;align-items:center;gap:34px;padding-left:28px;font-size:13px;font-weight:500}
.brand{position:absolute;left:500px;top:34px;width:200px;text-align:center}
.brand__dot{width:56px;height:56px;border-radius:50%;background:var(--ink);margin:0 auto 6px}
.brand__name{font-size:24px;font-weight:600;color:var(--ink);line-height:1;letter-spacing:1px;text-transform:uppercase}
.tools{position:absolute;left:700px;top:52px;width:343px;height:42px;border-top:1px solid var(--line);border-bottom:1px solid var(--line);display:flex;align-items:center;padding-left:38px;gap:10px;font-size:11px;color:var(--muted)}
.tools__search{flex:1;display:flex;align-items:center;gap:8px;height:100%;border-right:1px solid var(--line)}
.tools__icon{width:34px;display:flex;justify-content:center}

/* hero */
.hero{height:453px;position:relative;background:linear-gradient(100deg,#f3e4c6 0%,#f8eedb 45%,#f1dfbd 100%);overflow:hidden}
.hero__corner{position:absolute;left:-40px;top:-40px;width:90px;height:380px;border-radius:0 0 90px 0;background:var(--brown);transform:rotate(14deg)}
.hero__title{position:absolute;left:158px;top:76px;font-size:52px;font-weight:700;color:var(--brown);letter-spacing:1px}
.hero__script{position:absolute;left:152px;top:118px;font-size:100px;color:var(--teal);line-height:1}
.hero__text{position:absolute;left:158px;top:252px;width:430px;font-size:12.5px;line-height:1.5;color:var(--muted)}
.hero__btn{position:absolute;left:158px;top:338px;width:140px;height:46px;line-height:46px}
.hero__media{position:absolute;left:650px;top:0;width:640px;height:453px;border-radius:320px 0 0 320px;background:radial-gradient(circle at 50% 50%,#7b5033 0%,#4b2e1c 75%)}
.hero__dots{position:absolute;left:583px;top:598px;display:flex;gap:6px}
.hero__dots i{width:5px;height:5px;border-radius:50%;background:#cdbfa6}
.hero__dots i.on{background:var(--brown)}

/* features */
.features{height:230px;border-bottom:1px solid var(--line);display:flex;padding:20px 0 0 158px}
.feature{width:295px;text-align:center;padding-top:30px;border-right:1px solid var(--line);height:190px}
.feature:last-child{border-right:none}
.feature svg{display:block;margin:0 auto 16px}
.feature h3{font-size:16px;color:var(--orange);font-weight:500;letter-spacing:.3px;margin-bottom:10px}
.feature p{font-size:12.5px;color:var(--muted);line-height:1.5;width:200px;margin:0 auto}

/* section heads */
.head{text-align:center}
.head .script{font-size:24px;color:var(--teal)}
.head h2{font-size:36px;color:var(--brown);font-weight:700;letter-spacing:.5px;line-height:1.1}
.head p{font-size:13px;color:var(--ink);margin-top:10px}

/* product card */
.cards{display:flex;gap:29px}
.card{width:199px;position:relative}
.card__img{height:231px;border-radius:8px;position:relative;overflow:hidden}
.card__tag{position:absolute;right:14px;top:0;width:20px;height:48px;color:#fff;font-size:8px;font-weight:700;writing-mode:vertical-rl;transform:rotate(180deg);text-align:center;line-height:20px;clip-path:polygon(0 14%,50% 0,100% 14%,100% 100%,0 100%)}
.card__tag--new{background:#3e8a45}
.card__tag--sale{background:var(--sale)}
.card__actions{position:absolute;left:50%;top:50%;transform:translate(-50%,-50%);display:flex;gap:8px}
.card__actions span{width:28px;height:28px;border-radius:50%;background:#fff;display:flex;align-items:center;justify-content:center}
.card__name{font-size:15px;line-height:1.3;margin-top:18px;color:var(--ink)}
.card__stars{color:var(--teal);font-size:14px;letter-spacing:3px;margin-top:8px}
.card__price{font-size:20px;color:var(--brown);font-weight:500;margin-top:10px}
.card__price s{color:#a9a09a;margin-left:14px;font-weight:400}
.arrow{position:absolute;top:110px;color:#aaa;font-size:18px}

.arrivals{height:548px;padding-top:55px}
.arrivals .cards{margin-top:42px}

/* promos */
.promos{height:535px;position:relative;padding-top:54px}
.promo{position:absolute;overflow:hidden}
.promo--sign{left:0;top:54px;width:589px;height:481px;background:linear-gradient(160deg,#5d4a32 0%,#ece3d2 35%,#d8cbb3 70%,#6b5536 100%)}
.promo--tree{left:608px;top:54px;width:592px;height:233px;background:linear-gradient(90deg,#64a792 0%,#7db8a4 55%,#5a3d28 100%)}
.promo--gnome{left:608px;top:302px;width:592px;height:233px;background:linear-gradient(90deg,#8a5a35 0%,#a36c3f 60%,#84532f 100%)}
.promo__frame{position:absolute;left:18px;top:18px;right:18px;bottom:18px;border:1px solid rgba(255,255,255,.7)}
.promo__title{position:absolute;color:#fff;font-weight:700;font-size:32px;line-height:1}
.promo__script{position:absolute;color:#fff;font-size:64px;line-height:1}
.promo__btn{position:absolute;height:44px;line-height:44px}

/* gnome */
.gnome{height:459px;background:linear-gradient(100deg,#f6ecdb,#efe1c7);margin-top:25px;position:relative;overflow:hidden}
.gnome__intro{position:absolute;left:158px;top:70px;width:260px}
.gnome__intro .script{font-size:22px;color:var(--teal)}
.gnome__intro h2{font-size:36px;color:var(--brown);font-weight:700;margin-bottom:16px}
.gnome__intro p{font-size:12.5px;line-height:1.5;margin-bottom:14px}
.gnome__arrows{color:var(--teal);font-size:16px;letter-spacing:8px}
.gnome__cards{position:absolute;left:478px;top:74px;display:flex;gap:23px}
.gcard{width:261px;background:#fff;border-radius:6px;overflow:hidden}
.gcard .card__img{height:199px;border-radius:0}
.gcard__body{padding:18px 24px 22px}
.gcard__body .card__name{margin-top:0}

/* featured */
.featured{height:1064px;padding-top:70px}
.tabs{display:flex;justify-content:center;gap:36px;font-size:12.5px;color:var(--muted);margin-top:22px}
.tabs .on{color:var(--teal)}
.featured .cards{margin-top:34px}
.featured .cards + .cards{margin-top:42px}
.featured .card__img{height:233px}

/* spooky */
.spooky{height:305px;background:var(--teal);position:relative;overflow:hidden;margin-top:33px}
.spooky__media{position:absolute;left:0;top:0;width:650px;height:305px;border-radius:0 300px 300px 0;background:linear-gradient(90deg,#5a4c41 0%,#8b6f55 50%,#3d3128 100%)}
.spooky__title{position:absolute;left:760px;top:68px;color:#fff;font-size:32px;font-weight:600}
.spooky__script{position:absolute;left:757px;top:102px;color:#fff;font-size:72px;line-height:1}
.spooky__btn{position:absolute;left:760px;top:208px;width:138px;height:44px;line-height:44px}

/* testimonials */
.reviews{height:531px;padding-top:70px;position:relative}
.reviews .head h2{font-size:36px}
.tcard{position:absolute;top:195px;width:415px;height:200px;background:var(--cream);border-radius:6px;padding:26px 40px}
.tcard::before{content:"";position:absolute;right:0;top:-12px;width:190px;height:14px;background:var(--teal-dark);clip-path:polygon(0 100%,100% 0,100% 100%)}
.tcard__q{font-size:60px;color:var(--orange);font-weight:700;line-height:.6;height:32px}
.tcard__top{display:flex;justify-content:space-between;align-items:center;margin-top:8px}
.tcard__top .script{font-size:24px;color:var(--orange)}
.tcard__top .stars{color:var(--teal);letter-spacing:3px}
.tcard p{font-size:12.5px;font-style:italic;line-height:1.5;margin-top:12px}
.tcard__tail{position:absolute;left:30px;bottom:-18px;width:120px;height:20px;background:var(--teal-dark);clip-path:polygon(0 0,100% 0,60% 100%)}
.who{position:absolute;top:420px;display:flex;align-items:center;gap:12px;font-size:11px}
.who i{width:38px;height:38px;border-radius:50%;background:linear-gradient(#d6b79a,#8c6a50)}
.who b{color:var(--orange);font-weight:500;display:block}
.who span{color:var(--muted)}

/* newsletter */
.newsletter{height:119px;background:var(--orange);position:relative;color:#fff}
.newsletter h2{position:absolute;left:158px;top:34px;font-size:26px;font-weight:600;letter-spacing:.5px}
.newsletter p{position:absolute;left:158px;top:72px;font-size:12px}
.newsletter__input{position:absolute;left:617px;top:36px;width:297px;height:46px;background:#fff;border-radius:6px;color:#888;font-size:11px;display:flex;align-items:center;gap:8px;padding-left:18px}
.newsletter__btn{position:absolute;left:926px;top:36px;width:117px;height:46px;line-height:46px}

/* footer */
.footer{height:441px;background:linear-gradient(100deg,#f7efe1,#f1e5cf);position:relative}
.footer__brand{position:absolute;left:158px;top:60px;text-align:center;width:130px}
.footer__brand .brand__dot{width:48px;height:48px}
.footer__brand .brand__name{font-size:22px}
.contacts{position:absolute;left:420px;top:75px;font-size:12.5px;line-height:1.4}
.contacts li{list-style:none;display:flex;gap:8px;margin-bottom:6px;width:240px}
.social{display:flex;gap:12px;margin:14px 0 0 26px}
.social i{width:24px;height:24px;border-radius:50%;border:1.5px solid var(--brown)}
.account{position:absolute;left:770px;top:78px;font-size:12.5px}
.account h4{font-size:12px;color:var(--brown);font-weight:500;margin-bottom:16px}
.account__grid{display:grid;grid-template-columns:138px 130px;row-gap:10px}
.pay{position:absolute;left:0;width:1200px;top:296px;display:flex;justify-content:center;gap:30px;font-weight:700;font-size:18px;color:#333}
.fnav{position:absolute;left:0;width:1200px;top:356px;display:flex;justify-content:center;gap:22px;font-size:11.5px}
.copy{position:absolute;left:0;width:1200px;top:396px;text-align:center;font-size:11px;color:var(--muted)}
</style>
</head>
<body>

<div class="topbar">Get a free delivery over $50 order <span>→</span></div>

<header class="header">
  <nav class="nav"><span>PRODUCTS ⌄</span><span>FAQ</span><span>CONTACT US</span></nav>
  <div class="brand"><div class="brand__dot"></div><div class="brand__name">Copper<br>Lantern</div></div>
  <div class="tools">
    <div class="tools__search">
      <svg width="16" height="16" viewBox="0 0 16 16" fill="none" stroke="#333" stroke-width="1.5"><circle cx="7" cy="7" r="5"/><path d="M11 11l4 4"/></svg>
      Search entire store...
    </div>
    <div class="tools__icon"><svg width="16" height="16" viewBox="0 0 16 16" fill="none" stroke="#333" stroke-width="1.4"><path d="M3 5h10l-1 10H4z"/><path d="M6 5V3a2 2 0 014 0v2"/></svg></div>
    <div class="tools__icon"><svg width="16" height="16" viewBox="0 0 16 16" fill="none" stroke="#333" stroke-width="1.4"><circle cx="8" cy="5" r="3"/><path d="M2 15c1-4 11-4 12 0"/></svg></div>
  </div>
</header>

<section class="hero">
  <div class="hero__corner"></div>
  <h1 class="hero__title">PERSONALIZED</h1>
  <div class="hero__script script">Ornaments</div>
  <p class="hero__text">Sed ut perspiciatis unde omnis iste natus error sit volup tatem acc usantium doloremque laudantium, totam rem aperiam, eaque ipsa quae ab illo inventore veritatis et quasi</p>
  <span class="btn btn--teal hero__btn">Shop now</span>
  <div class="hero__media" role="img" aria-label="Wooden dinosaur name ornaments hanging on a pine branch"></div>
</section>
<div class="hero__dots"><i></i><i class="on"></i><i></i></div>

<section class="features">
  <div class="feature">
    <svg width="52" height="48" viewBox="0 0 52 48" fill="none" stroke="var(--orange)" stroke-width="2"><path d="M6 14l20-8 20 8v20l-20 8-20-8z"/><path d="M6 14l20 8 20-8M26 22v20"/><circle cx="40" cy="36" r="7" fill="#fff"/><path d="M37 36a3 3 0 116 0"/></svg>
    <h3>RETURN &amp; EXCHANGE</h3><p>Committed to return the money in 30 days</p>
  </div>
  <div class="feature">
    <svg width="52" height="48" viewBox="0 0 52 48" fill="none" stroke="var(--orange)" stroke-width="2"><path d="M8 20l30-14-6 12 10 4-30 14 6-12z"/><rect x="26" y="30" width="20" height="14"/><path d="M36 30v14"/></svg>
    <h3>WORLDWIDE SHIPPING</h3><p>No place in the world can stop us bringing goods.</p>
  </div>
  <div class="feature">
    <svg width="52" height="48" viewBox="0 0 52 48" fill="none" stroke="var(--orange)" stroke-width="2"><path d="M10 26v-6a16 16 0 0132 0v6"/><rect x="6" y="24" width="8" height="12" rx="3"/><rect x="38" y="24" width="8" height="12" rx="3"/><path d="M42 36c0 6-6 8-14 8"/><circle cx="20" cy="24" r="1.5"/><circle cx="26" cy="24" r="1.5"/><circle cx="32" cy="24" r="1.5"/></svg>
    <h3>ONLINE SUPPORT 24/7</h3><p>24/7 online support is always ready always</p>
  </div>
</section>

<section class="arrivals">
  <div class="container">
    <div class="head">
      <div class="script">Trending decor in this season</div>
      <h2>NEW ARRIVALS</h2>
      <p>Discover our unique products</p>
    </div>
    <span class="arrow" style="left:-40px;top:260px">←</span>
    <span class="arrow" style="right:-40px;top:260px;color:var(--teal)">→</span>
    <div class="cards">
      <div class="card">
        <div class="card__img" role="img" aria-label="Round paw print memorial ornament with angel wings" style="background:linear-gradient(#8f6a55,#e9cfc6 40%,#6e4b36)"><span class="card__tag card__tag--new">NEW</span></div>
        <div class="card__name">In Memory of Lost Pet Ornament</div>
        <div class="card__price">$16.00</div>
      </div>
      <div class="card">
        <div class="card__img" role="img" aria-label="Framed wooden family tree with grandkids names" style="background:linear-gradient(#4a3a2c,#cfc4b2 50%,#4a3a2c)"><span class="card__tag card__tag--sale">SALE</span></div>
        <div class="card__name">12 Inch Square Framed Personalized Family...</div>
        <div class="card__price">$62.00<s>$72.00</s></div>
      </div>
      <div class="card">
        <div class="card__img" role="img" aria-label="Faux shiplap family tree sign in warm wood" style="background:linear-gradient(#b07a48,#8c5a30)"><span class="card__tag card__tag--new">NEW</span>
          <div class="card__actions"><span><svg width="12" height="12" viewBox="0 0 12 12" fill="none" stroke="var(--teal)" stroke-width="1.3"><path d="M6 10L2 6a2.2 2.2 0 014-3 2.2 2.2 0 014 3z"/></svg></span><span><svg width="12" height="12" viewBox="0 0 12 12" fill="none" stroke="var(--teal)" stroke-width="1.3"><path d="M2 4h8l-1 7H3z"/><path d="M4 4V3a2 2 0 014 0v1"/></svg></span></div>
        </div>
        <div class="card__name">Faux Shiplap Personalized Family Tree</div>
        <div class="card__price">$69.00</div>
      </div>
      <div class="card">
        <div class="card__img" role="img" aria-label="Custom family Christmas ornament set with hanging names" style="background:linear-gradient(#e4d8d0,#caa79a)"><span class="card__tag card__tag--new">NEW</span></div>
        <div class="card__name">Custom Family Christmas Ornament –</div>
        <div class="card__price">$26.00</div>
      </div>
    </div>
  </div>
</section>

<section class="promos">
  <div class="promo promo--sign" role="img" aria-label="Person holding a personalized wooden family name sign">
    <div class="promo__frame"></div>
    <div class="promo__title" style="left:44px;top:348px;color:#fff">PERSONALIZED</div>
    <div class="promo__script script" style="left:40px;top:376px">Family sign</div>
    <span class="btn btn--teal promo__btn" style="left:408px;top:386px;width:138px">Shop now</span>
  </div>
  <div class="promo promo--tree" role="img" aria-label="Teal layered wooden family tree frame">
    <div class="promo__title" style="left:42px;top:56px;font-size:30px">FAMILY<br>TREE FRAME</div>
    <span class="btn btn--orange promo__btn" style="left:42px;top:136px;width:136px">Shop now</span>
  </div>
  <div class="promo promo--gnome" role="img" aria-label="Two painted wooden gnomes with red hats">
    <div class="promo__title" style="left:366px;top:56px;font-size:30px">GNOME<br>HANDS</div>
    <span class="btn btn--teal promo__btn" style="left:366px;top:136px;width:168px">View products</span>
  </div>
</section>

<section class="gnome">
  <div class="gnome__intro">
    <div class="script">Copper Lantern</div>
    <h2>GNOME</h2>
    <p>Lorem ipsum dolor sit amet, consectetur adipiscing elit, sed do eiusmod tempor incididunt ut labore et dolore magna ali qua. Ut enim ad minim veniam, quis nos trud exercitation ullamco</p>
    <p>Duis aute irure dolor in reprehenderit in voluptate velit esse cillum dolore eu fugiat nulla pariatur.</p>
    <div class="gnome__arrows">← →</div>
  </div>
  <div class="gnome__cards">
    <div class="gcard">
      <div class="card__img" role="img" aria-label="Bee themed wooden wall art on a shelf" style="background:linear-gradient(#9a8f83,#3d3027 50%,#c9b79f)"></div>
      <div class="gcard__body"><div class="card__name">Bee Happy Bee Kind Bee You Wooden Wall Art...</div><div class="card__price">$47.00</div></div>
    </div>
    <div class="gcard">
      <div class="card__img" role="img" aria-label="Halloween wooden lamp with pumpkins" style="background:linear-gradient(#6a4027,#9c6235)"><span class="card__tag card__tag--new">NEW</span>
        <div class="card__actions"><span><svg width="12" height="12" viewBox="0 0 12 12" fill="none" stroke="var(--teal)" stroke-width="1.3"><path d="M6 10L2 6a2.2 2.2 0 014-3 2.2 2.2 0 014 3z"/></svg></span><span><svg width="12" height="12" viewBox="0 0 12 12" fill="none" stroke="var(--teal)" stroke-width="1.3"><path d="M2 4h8l-1 7H3z"/><path d="M4 4V3a2 2 0 014 0v1"/></svg></span></div>
      </div>
      <div class="gcard__body"><div class="card__name">Halloween Wooden Lamp, Jack O Lantern...</div><div class="card__price">$24.00</div></div>
    </div>
    <div class="gcard">
      <div class="card__img" role="img" aria-label="Stack of round birch plywood blanks" style="background:linear-gradient(#8a7a6c,#dcd2c5)"></div>
      <div class="gcard__body"><div class="card__name">Premium Baltic Birch Plywood 11.75...</div><div class="card__price">$36.00</div></div>
    </div>
  </div>
</section>

<section class="featured">
  <div class="container">
    <div class="head">
      <div class="script">Trending decor in this season</div>
      <h2>FEATURED PRODUCTS</h2>
    </div>
    <div class="tabs"><span>LATEST</span><span class="on">TOP RATED</span><span>BEST SELLING</span></div>
    <div class="cards">
      <div class="card"><div class="card__img" role="img" aria-label="Wooden heart name pieces" style="background:linear-gradient(#e8dccb,#c9a06c)"></div><div class="card__name">Personalized Hearts For Your Family Tree</div><div class="card__stars">★★★★★</div><div class="card__price">$5.00 – $11.75</div></div>
      <div class="card"><div class="card__img" role="img" aria-label="Paw print memorial ornament" style="background:linear-gradient(#8f6a55,#e9cfc6 40%,#6e4b36)"></div><div class="card__name">In Memory Of Lost Pet Ornament</div><div class="card__stars">★★★★★</div><div class="card__price">$16.00 – $22.00</div></div>
      <div class="card"><div class="card__img" role="img" aria-label="Framed family tree in wood" style="background:linear-gradient(#b07a48,#8c5a30)">
        <div class="card__actions"><span><svg width="12" height="12" viewBox="0 0 12 12" fill="none" stroke="var(--teal)" stroke-width="1.3"><path d="M6 10L2 6a2.2 2.2 0 014-3 2.2 2.2 0 014 3z"/></svg></span><span><svg width="12" height="12" viewBox="0 0 12 12" fill="none" stroke="var(--teal)" stroke-width="1.3"><path d="M2 4h8l-1 7H3z"/><path d="M4 4V3a2 2 0 014 0v1"/></svg></span></div>
      </div><div class="card__name">12 Inch Square Framed Personalized Family...</div><div class="card__stars">★★★★★</div><div class="card__price">$62.00 – $80.00</div></div>
      <div class="card"><div class="card__img" role="img" aria-label="Blank wooden mushroom shape" style="background:linear-gradient(#7d6f64,#e8e4df 40%,#c9c2ba)"></div><div class="card__name">Mushroom – Interchangeable Piece...</div><div class="card__stars">★★★★★</div><div class="card__price">$3.00 – $5.00</div></div>
    </div>
    <div class="cards">
      <div class="card"><div class="card__img" role="img" aria-label="Blank wooden watermelon slice shape" style="background:linear-gradient(#ded8d0,#b9ada0)"></div><div class="card__name">Watermellon – Interchangeable Piece...</div><div class="card__stars">★★★★★</div><div class="card__price">$3.00 – $5.75</div></div>
      <div class="card"><div class="card__img" role="img" aria-label="Shiplap family tree sign" style="background:linear-gradient(#5a4634,#e2d6c2 40%,#c6b196)"></div><div class="card__name">Faux Shiplap Personalized Family Tree</div><div class="card__stars">★★★★★</div><div class="card__price">$69.00 – $75.00</div></div>
      <div class="card"><div class="card__img" role="img" aria-label="Pet memorial plaque on a stand" style="background:linear-gradient(#b8c3c9,#f1eeea 50%,#a9a39b)"></div><div class="card__name">In Memory of Lost Pet Plaque, Custom...</div><div class="card__stars">★★★★★</div><div class="card__price">$62.00 – $80.00</div></div>
      <div class="card"><div class="card__img" role="img" aria-label="Many wooden Christmas name ornaments" style="background:linear-gradient(#7c5c48,#e2cdbf 45%,#9b7862)"></div><div class="card__name">Custom Family Christmas Ornament...</div><div class="card__stars">★★★★★</div><div class="card__price">$3.00 – $5.00</div></div>
    </div>
  </div>
</section>

<section class="spooky">
  <div class="spooky__media" role="img" aria-label="Halloween tiered tray with boo and trick or treat signs"></div>
  <div class="spooky__title">TIERED TRAY DECOR</div>
  <div class="spooky__script script">Spooky decor</div>
  <span class="btn btn--orange spooky__btn">Shop now</span>
</section>

<section class="reviews">
  <div class="container" style="height:100%">
    <div class="head">
      <div class="script">Find out why people love copperlantern</div>
      <h2>WHAT PEOPLE SAY</h2>
    </div>
    <span class="arrow" style="left:-40px;top:190px">←</span>
    <span class="arrow" style="right:-40px;top:190px;color:var(--teal)">→</span>
    <div class="tcard" style="left:0">
      <div class="tcard__q">“</div>
      <div class="tcard__top"><span class="script">Excellent Products</span><span class="stars">★★★★★</span></div>
      <p>Lorem ipsum dolor sit amet, consectetur adipiscing elit, sed do eiusmod tempor incididunt ut labore et dolore magna ali qua. Ut enim ad minim veniam, quis nos trud exercitation ullamco.</p>
      <div class="tcard__tail"></div>
    </div>
    <div class="tcard" style="left:460px">
      <div class="tcard__q">“</div>
      <div class="tcard__top"><span class="script">Much Recommended</span><span class="stars">★★★★★</span></div>
      <p>Lorem ipsum dolor sit amet, consectetur adipiscing elit, sed do eiusmod tempor incididunt ut labore et dolore magna ali qua. Ut enim ad minim veniam, quis nos trud exercitation ullamco.</p>
      <div class="tcard__tail"></div>
    </div>
    <div class="who" style="left:68px"><i role="img" aria-label="Customer portrait"></i><div><b>MARA QUINN</b><span>USA</span></div></div>
    <div class="who" style="left:528px"><i role="img" aria-label="Customer portrait"></i><div><b>LENA BROOKS</b><span>USA</span></div></div>
  </div>
</section>

<section class="newsletter">
  <h2>SIGN UP TO OUR NEWSLETTER!</h2>
  <p>Don't miss latest updates &amp; hot deals</p>
  <div class="newsletter__input"><svg width="14" height="12" viewBox="0 0 14 12" fill="none" stroke="#999" stroke-width="1.2"><rect x="1" y="1" width="12" height="10"/><path d="M1 1l6 5 6-5"/></svg>Enter your email</div>
  <span class="btn btn--teal newsletter__btn">Subscribe</span>
</section>

<footer class="footer">
  <div class="footer__brand"><div class="brand__dot"></div><div class="brand__name">Copper<br>Lantern</div></div>
  <ul class="contacts">
    <li><svg width="14" height="14" viewBox="0 0 14 14" fill="none" stroke="var(--teal)" stroke-width="1.3"><path d="M3 1h3l1 3-2 1a7 7 0 004 4l1-2 3 1v3a1 1 0 01-1 1A12 12 0 012 2a1 1 0 011-1z"/></svg>(+012) 555-0148</li>
    <li><svg width="14" height="14" viewBox="0 0 14 14" fill="none" stroke="var(--teal)" stroke-width="1.3"><rect x="1" y="3" width="12" height="9"/><path d="M1 3l6 5 6-5"/></svg>support@copperlantern.com</li>
    <li><svg width="14" height="14" viewBox="0 0 14 14" fill="none" stroke="var(--teal)" stroke-width="1.3"><path d="M7 13s-4.5-4.5-4.5-7.5a4.5 4.5 0 019 0C11.5 8.5 7 13 7 13z"/><circle cx="7" cy="5.5" r="1.6"/></svg>123, Lorem ipsum dolor sit amet, consectetur Adipiscing</li>
    <div class="social"><i></i><i></i><i></i></div>
  </ul>
  <div class="account">
    <h4>MY ACCOUNT</h4>
    <div class="account__grid"><span>My orders</span><span>My personal info</span><span>My credit slips</span><span>My Account</span><span>My addresses</span><span>Track your Order</span></div>
  </div>
  <div class="pay"><span>Paycard</span><span>Duocard</span><span>WalletPay</span></div>
  <nav class="fnav"><span>HOME</span><span>HOME DECOR</span><span>GNOME</span><span>PERSONALIZED GIFTS</span><span>CRAFT SUPPLIES</span><span>PRE-CUT SHAPES</span><span>UNFINISHED WOOD</span><span>HALLOWEEN</span></nav>
  <div class="copy">Copyright 2022 © Copper Lantern</div>
</footer>

</body>
</html>
```